Building company requiring web site design

We need a web design for a new company based in Sydney called Marlow Building Co. We build and renovate new and existing homes for consumers. We would like to see design that use the colours red and grey. The final design should communicate innovative building but with old fashion quality, great customer service and attention to detail. I have already had a logo and stationary design completed and would like to use the these colour schemes
Updates

Target Market(s)

Home owners, investors

Industry/Entity Type

Building

Coding

Coded - Design and coding required

Number of Pages Required

5+ page

Requirements
Must have
• Home page, contact page, about us page, gallery page and testimonial page
Nice to have
• Contact form

```html
<!DOCTYPE html>
<html lang="en">
<head>
<meta charset="utf-8">
<title>Marlow Building Co.</title>
<link href="https://fonts.googleapis.com/css2?family=Bree+Serif&family=Open+Sans:ital,wght@0,400;0,600;0,700;1,400&family=Roboto:wght@400;500;700&display=swap" rel="stylesheet">
<style>
:root{
  --red:#b94a48;
  --red-dark:#a33d3b;
  --charcoal:#2f2f33;
  --charcoal-deep:#2a2a2e;
  --topbar:#262628;
  --text:#555;
  --heading:#222;
  --white:#fff;
  --light-line:#eee;
}
*{box-sizing:border-box;margin:0;padding:0}
html,body{width:1200px;height:3232px;overflow:hidden}
body{font-family:"Open Sans",Arial,sans-serif;color:var(--text);background:var(--white);position:relative}
section,header,footer,div{position:relative}

/* top bar */
.topbar{height:38px;background:var(--topbar);color:#ddd;font-size:12px}
.topbar .social{position:absolute;left:62px;top:10px;display:flex;gap:6px}
.dot{width:17px;height:17px;border-radius:50%;background:#5a5a5e;display:block}
.topbar .links{position:absolute;right:62px;top:0;height:38px;display:flex;align-items:center;gap:28px}
.topbar .links span{display:flex;align-items:center;gap:8px}

/* header */
.site-header{height:147px;background:var(--white)}
.brand{position:absolute;left:60px;top:55px;display:flex;align-items:center;gap:12px}
.brand-square{width:34px;height:34px;background:var(--red)}
.brand-name{font-family:"Bree Serif",Georgia,serif;font-size:24px;color:var(--charcoal)}
.nav{position:absolute;right:60px;top:55px;display:flex;gap:6px;font-family:"Roboto",Arial,sans-serif;font-size:13px;font-weight:500;color:#222}
.nav a{display:block;padding:10px 12px;color:inherit;text-decoration:none}
.nav a.active{background:var(--red);color:var(--white)}

/* hero */
.hero{height:563px;background:
  radial-gradient(ellipse 380px 300px at 260px 300px,rgba(214,170,60,.55),transparent 70%),
  radial-gradient(ellipse 300px 260px at 780px 320px,rgba(70,120,180,.45),transparent 70%),
  linear-gradient(180deg,#8a5a44 0%,#a87458 35%,#c9a57e 70%,#9a7a5c 100%)}
.hero-caption{position:absolute;left:571px;top:263px;width:571px;height:86px;background:rgba(25,25,25,.85);color:var(--white);font-family:"Bree Serif",Georgia,serif;font-size:36px;letter-spacing:1px;display:flex;align-items:center;justify-content:center}
.hero-btn{position:absolute;left:993px;top:360px;width:147px;height:52px;background:var(--red);color:var(--white);font-size:18px;display:flex;align-items:center;justify-content:center}
.slider-dots{position:absolute;display:flex;gap:5px}
.slider-dots i{width:10px;height:10px;border-radius:50%;background:#222;display:block}
.slider-dots i.on{background:var(--red)}

/* offer */
.offer{height:520px}
.offer-photo{position:absolute;left:54px;top:49px;width:452px;height:471px;background:
  radial-gradient(ellipse 200px 120px at 380px 230px,rgba(40,50,90,.55),transparent 75%),
  radial-gradient(ellipse 220px 60px at 220px 60px,rgba(240,200,40,.45),transparent 75%),
  linear-gradient(180deg,#fff 0%,#e8e2d8 30%,#c9955c 70%,#b07a46 100%)}
.eyebrow{color:var(--red);font-size:13px}
.section-title{font-family:"Bree Serif",Georgia,serif;color:var(--heading);font-weight:400}
.rule{width:60px;height:3px;background:var(--red)}
.offer .eyebrow{position:absolute;left:582px;top:46px}
.offer .section-title{position:absolute;left:580px;top:66px;font-size:40px}
.offer .rule{position:absolute;left:582px;top:123px}
.offer-text{position:absolute;left:582px;top:160px;width:560px;font-size:13px;line-height:22px;color:#666}
.offer-icon{position:absolute;left:586px;top:329px}
.outline-btn{position:absolute;border:2px solid var(--red);color:var(--red);font-size:12px;font-weight:600;display:flex;align-items:center;justify-content:center;letter-spacing:.3px}

/* quote band */
.quote-band{height:105px;background:var(--charcoal)}
.quote-band .eyebrow{position:absolute;left:60px;top:30px;font-size:15px}
.quote-band h2{position:absolute;left:60px;top:52px;color:var(--white);font-family:"Open Sans",Arial,sans-serif;font-size:24px;font-weight:700}
.solid-btn{position:absolute;left:978px;top:29px;width:162px;height:48px;background:var(--red);color:var(--white);font-size:14px;display:flex;align-items:center;justify-content:center;gap:10px}

/* shared centred heading block */
.centered{position:absolute;left:0;width:1200px;text-align:center}
.section-rule{position:absolute;left:570px}

/* what we do */
.services{height:687px}
.services .eyebrow{top:80px;font-size:15px}
.services .section-title{top:106px;font-size:40px}
.card{position:absolute;top:224px;width:337px}
.card-photo{height:245px}
.card .tag{margin-top:20px;color:var(--red);font-size:12px}
.card h3{margin-top:6px;font-family:"Open Sans",Arial,sans-serif;font-weight:700;font-size:28px;color:var(--heading);letter-spacing:.5px}
.card-rule{margin-top:6px;width:36px;height:3px;background:var(--red)}

/* cta */
.cta{height:336px;background:
  radial-gradient(ellipse 300px 200px at 420px 80px,rgba(230,170,140,.6),transparent 70%),
  linear-gradient(110deg,#c06a58 0%,#d48c74 45%,#c7806a 70%,#b0604f 100%)}
.cta h2{top:88px;color:var(--white);font-family:"Open Sans",Arial,sans-serif;font-weight:700;font-size:32px;line-height:38px}
.cta .btn{position:absolute;top:205px;width:138px;height:48px;display:flex;align-items:center;justify-content:center;font-size:14px}
.cta .btn.ghost{left:465px;border:2px solid var(--white);color:var(--white)}
.cta .btn.fill{left:616px;background:var(--white);color:#333}

/* partners */
.partners{height:442px}
.partners .eyebrow{top:106px;font-size:15px}
.partners .section-title{top:134px;font-size:40px}
.partner-row{position:absolute;left:78px;top:245px;display:flex;gap:11px}
.partner{width:200px;height:129px;border:1px solid var(--light-line);display:flex;align-items:center;justify-content:center}
.partner span{width:70px;height:70px;border-radius:50%;background:#e3e3e3;display:block}

/* hours */
.hours{height:71px;background:var(--red);color:var(--white);font-size:16px}
.hours .left{position:absolute;left:62px;top:0;height:71px;display:flex;align-items:center;gap:12px}
.hours .right{position:absolute;right:62px;top:0;height:71px;display:flex;align-items:center;gap:14px}
.hours .dot{background:rgba(255,255,255,.85);width:18px;height:18px}

/* footer */
.site-footer{height:323px;background:var(--charcoal-deep);color:#ddd;font-family:"Roboto",Arial,sans-serif;font-size:13px}
.col{position:absolute;top:24px}
.col h4{font-size:16px;font-weight:700;color:var(--white);letter-spacing:.3px}
.col .rule{width:40px;margin-top:8px}
.col p{margin-top:22px;line-height:19px;width:330px}
.col ul{list-style:none;line-height:23px}
.svc-lists{display:flex;gap:46px;margin-top:22px}
.newsletter{margin-top:24px;display:flex}
.newsletter .join{width:60px;height:34px;background:var(--red);color:var(--white);display:flex;align-items:center;justify-content:center;font-size:13px}
.newsletter .field{width:200px;height:34px;background:var(--white);color:#888;font-size:13px;display:flex;align-items:center;padding-left:8px}
.footer-social{margin-top:12px;display:flex;gap:6px}
.footer-social i{width:18px;height:18px;display:block;background:#4a6fa5}
.footer-social i:nth-child(2){background:#c86a3d}
.footer-social i:nth-child(3){background:#c04a3c}
.footer-social i:nth-child(4){background:#3b5b9a}
.copyright{position:absolute;left:0;top:263px;width:1200px;border-top:1px solid #3c3c40;padding-top:20px;text-align:center;font-size:13px;color:#ddd}
</style>
</head>
<body>

<div class="topbar">
  <div class="social"><i class="dot"></i><i class="dot"></i><i class="dot"></i><i class="dot"></i><i class="dot"></i></div>
  <div class="links">
    <span><svg width="16" height="16" viewBox="0 0 16 16"><circle cx="8" cy="8" r="8" fill="#5a5a5e"/><path d="M5 4.5l2 2-1 1c.6 1.2 1.4 2 2.5 2.5l1-1 2 2-1.2 1.2C7 12 4 9 3.8 5.7z" fill="#fff"/></svg>+1 555-010-2040</span>
    <span><svg width="18" height="14" viewBox="0 0 18 14"><rect x="1" y="2" width="16" height="10" rx="1" fill="#777"/><path d="M1 3l8 5 8-5" stroke="#262628" fill="none"/></svg>WebMail</span>
    <span><svg width="18" height="14" viewBox="0 0 18 14"><ellipse cx="9" cy="6" rx="8" ry="5" fill="#777"/><path d="M4 10l-1 4 4-3z" fill="#777"/></svg>LiveChat</span>
    <span><svg width="14" height="14" viewBox="0 0 14 14"><circle cx="7" cy="7" r="7" fill="#777"/><text x="7" y="11" font-size="10" text-anchor="middle" fill="#262628" font-family="Arial,sans-serif">?</text></svg>Support</span>
  </div>
</div>

<header class="site-header">
  <div class="brand"><span class="brand-square"></span><span class="brand-name">Marlow Building Co.</span></div>
  <nav class="nav">
    <a class="active">HOME</a><a>SERVICES</a><a>PROJECTS</a><a>OUR TEAM</a><a>BLOG</a><a>COST</a><a>CALCULATOR</a><a>CONTACT</a>
  </nav>
</header>

<section class="hero" role="img" aria-label="Photo of a builder in a hard hat showing house plans to a smiling couple outside a home">
  <div class="hero-caption">RENOVATING YOUR HOME</div>
  <div class="hero-btn">Read More</div>
  <div class="slider-dots" style="left:616px;top:524px"><i class="on"></i><i></i><i></i><i></i></div>
</section>

<section class="offer">
  <div class="offer-photo" role="img" aria-label="Photo of four smiling builders in hard hats and tool belts"></div>
  <p class="eyebrow">Develops quality projects to cater for workplace and office</p>
  <h2 class="section-title">GET OFFER</h2>
  <div class="rule"></div>
  <p class="offer-text">Our customers, employees and subcontractors are the reasons for our existence. We will take all necessary precautions in order to render our work environments more secure and healthy and we will prioritize maintenance of such precautions. We will abide by the legal legislations and work safety regulations in effect at our country and in other countries where we are active.</p>
  <svg class="offer-icon" width="114" height="115" viewBox="0 0 114 115">
    <path d="M20 0h60l14 14v60H20z" fill="var(--red)"/>
    <path d="M0 40h40l8 8h66l-10 67H0z" fill="var(--red-dark)"/>
  </svg>
  <div class="outline-btn" style="left:743px;top:347px;width:207px;height:43px">DOWNLOAD PDF CATALOG</div>
  <div class="outline-btn" style="left:743px;top:401px;width:162px;height:43px">SEE COLOR SCHEME</div>
</section>

<section class="quote-band">
  <p class="eyebrow">We contribute to the society with the ones we protect</p>
  <h2>DEVELOP AS WELL AS THE ONES WE PROVIDE FOR OUR CUSTOMERS</h2>
  <div class="solid-btn">GET A QUOTE <svg width="8" height="12" viewBox="0 0 8 12"><path d="M1 1l5 5-5 5" stroke="#fff" stroke-width="2" fill="none"/></svg></div>
</section>

<section class="services">
  <p class="eyebrow centered">Don't be an architecture of building, be the architecture of life.</p>
  <h2 class="section-title centered">WHAT WE DO</h2>
  <div class="rule section-rule" style="top:170px"></div>
  <div class="card" style="left:58px">
    <div class="card-photo" role="img" aria-label="Photo of a carpenter at work under a red overlay" style="background:radial-gradient(ellipse 120px 90px at 150px 60px,rgba(230,170,110,.6),transparent 70%),linear-gradient(135deg,#c98a72,#b8665a)">
      <svg style="position:absolute;left:161px;top:115px" width="16" height="16" viewBox="0 0 16 16"><path d="M8 0v16M0 8h16" stroke="#fff" stroke-width="2"/></svg>
    </div>
    <p class="tag">develop and recreate as well as the ones we provide</p>
    <h3>CONTRACTING</h3><div class="card-rule"></div>
  </div>
  <div class="card" style="left:431px">
    <div class="card-photo" role="img" aria-label="Photo of a bricklayer in a hi-vis vest laying bricks" style="background:radial-gradient(ellipse 70px 60px at 190px 80px,rgba(220,220,90,.55),transparent 75%),linear-gradient(180deg,#c8cfd8 0%,#8a5a45 55%,#a24f35 80%,#6b4534 100%)"></div>
    <p class="tag">develop and recreate as well as the ones we provide</p>
    <h3>ARCHITECTURE</h3><div class="card-rule"></div>
  </div>
  <div class="card" style="left:803px">
    <div class="card-photo" role="img" aria-label="Photo of a worker in a hard hat using a power drill on timber" style="background:radial-gradient(ellipse 70px 50px at 150px 110px,rgba(240,200,40,.6),transparent 75%),linear-gradient(100deg,#c49a6c 0%,#b89470 30%,#6d8fb8 55%,#7a5a40 100%)"></div>
    <p class="tag">develop and recreate as well as the ones we provide</p>
    <h3>INTERIOR DESIGN</h3><div class="card-rule"></div>
  </div>
  <div class="slider-dots" style="left:612px;top:594px"><i class="on"></i><i></i></div>
</section>

<section class="cta" role="img" aria-label="Photo of hands working on timber with carpentry tools under a red overlay">
  <h2 class="centered">Looking for a quality and afforable<br>construction services for your next project?</h2>
  <div class="btn ghost">Learn More</div>
  <div class="btn fill">Contact Us</div>
</section>

<section class="partners">
  <p class="eyebrow centered">Happy to introduce our amazing project partners</p>
  <h2 class="section-title centered">PARTNERSHIP</h2>
  <div class="rule section-rule" style="top:192px"></div>
  <div class="partner-row">
    <div class="partner"><span></span></div>
    <div class="partner"><span></span></div>
    <div class="partner"><span></span></div>
    <div class="partner"><span></span></div>
    <div class="partner"><span></span></div>
  </div>
</section>

<div class="hours">
  <div class="left"><svg width="22" height="22" viewBox="0 0 22 22"><circle cx="11" cy="12" r="9" fill="none" stroke="#fff" stroke-width="2"/><path d="M11 7v5l3 2" stroke="#fff" stroke-width="2" fill="none"/></svg>Monday to Saturday: 9:00 - 18:00 // Sunday: Closed</div>
  <div class="right">Follow us on social media <i class="dot"></i><i class="dot"></i><i class="dot"></i></div>
</div>

<footer class="site-footer">
  <div class="col" style="left:75px">
    <h4>ABOUT BUILDER</h4><div class="rule"></div>
    <p>Our construction management professionals organize, lead and manage the people, materials and processes of construction utilizing construction management professionals</p>
    <p style="margin-top:18px">Our construction management professionals organize, lead and manage the people, materials and</p>
  </div>
  <div class="col" style="left:435px">
    <h4>OUR SERVICES</h4><div class="rule"></div>
    <div class="svc-lists">
      <ul><li>House Renovation</li><li>Metal Roofing</li><li>General Contracting</li><li>Lamite Flooring</li><li>Condo Remodoling</li><li>Artchitecture</li></ul>
      <ul><li>Lamite Flooring</li><li>Artchitecture</li><li>House Renovation</li><li>Interior Design</li><li>Metal Roofing</li><li>General Contracting</li></ul>
    </div>
  </div>
  <div class="col" style="left:795px">
    <h4>JOIN NEWSLETTER</h4><div class="rule"></div>
    <p>Our construction management professionals organize, lead and manage</p>
    <div class="newsletter"><span class="join">JOIN</span><span class="field">Type your e-mail</span></div>
    <div class="footer-social"><i></i><i></i><i></i><i></i></div>
  </div>
  <p class="copyright">© 2016 Marlow Building Co. All Right Reserved.</p>
</footer>

</body>
</html>
```